Contemporary Media Company with Logo Needs Business Card Design

Need a modern card design for a full service digital media company using the logo included. Also want the info below on the card. Probably list the services on the card back to save space for the front. Want something contemporary to impress prospective clients. You may want to submit both a somewhat more conservative design, and then a more wild one.
General Info: (this phrase need not be on the card)
Ned Parlow
Founder and CEO
949-612-4830
ned@vontaramedia.example
vontaramedia.example
Services: (this word need not be on the card)
Content & Experience Strategy
Brand Development
Search Engine Optimization
Website Design
Website Operation
Social Media Integration
Complete Video Solutions
Updates
Industry/Entity Type
Business
Contact Information for Business Card
Ned Parlow
Founder and CEO
949-612-4830
ned@vontaramedia.example
vontaramedia.example
Brand Development
Website Design
Website Operation
Social Media Integration
Complete Video Solutions
Look and feel
Each slider illustrates characteristics of the customer's brand and the style your logo design should communicate.

```html
<!DOCTYPE html>
<html lang="en">
<head>
<meta charset="utf-8">
<title>Vontara Media – Business Card</title>
<link rel="stylesheet" href="https://fonts.googleapis.com/css2?family=Source+Sans+3:ital,wght@0,400;0,600;1,400&display=swap">
<style>
  :root {
    --backdrop: #939394;
    --card: #2d2d2f;
    --orange: #d8681f;
    --grey-text: #a9a9ac;
    --light-text: #e4e4e6;
    --brand-grey: #8e8e92;
  }
  * { margin: 0; padding: 0; box-sizing: border-box; }
  html, body {
    width: 1105px; height: 1200px; overflow: hidden;
    background: var(--backdrop);
    font-family: "Source Sans 3", "Myriad Pro", Arial, sans-serif;
  }
  .card {
    position: absolute; left: 182px; width: 746px; height: 427px;
    background: var(--card);
  }
  .card--front { top: 119px; }
  .card--back { top: 637px; }

  .brand-square {
    position: absolute; left: 48px; top: 78px;
    width: 270px; height: 270px; background: var(--orange);
  }

  .contact {
    position: absolute; right: 34px; top: 26px; text-align: right;
  }
  .contact__name { color: var(--orange); font-size: 25px; font-weight: 600; line-height: 1.2; }
  .contact__title { color: var(--grey-text); font-size: 19px; line-height: 1.35; margin-bottom: 8px; }
  .contact__line {
    display: flex; justify-content: flex-end; align-items: center; gap: 10px;
    color: var(--light-text); font-size: 19px; line-height: 28px;
  }
  .contact__line svg { width: 17px; height: 17px; fill: var(--orange); flex: none; }

  .wordmark {
    color: var(--brand-grey); font-weight: 400; white-space: nowrap;
    text-transform: uppercase; letter-spacing: 0.06em;
  }
  .card--front .wordmark {
    position: absolute; right: 34px; top: 196px; font-size: 40px;
  }

  .services {
    position: absolute; right: 34px; top: 282px; list-style: none; text-align: right;
    color: var(--light-text); font-style: italic; font-size: 17.5px; line-height: 23.6px;
  }

  .back-brand {
    position: absolute; left: 0; right: 0; top: 0; bottom: 0;
    display: flex; align-items: center; justify-content: center; gap: 26px;
  }
  .back-brand__square { width: 62px; height: 62px; background: var(--orange); }
  .card--back .wordmark { font-size: 44px; }
</style>
</head>
<body>
  <section class="card card--front">
    <div class="brand-square"></div>

    <div class="contact">
      <p class="contact__name">Ned Parlow</p>
      <p class="contact__title">Founder and CEO</p>
      <p class="contact__line">949-612-4830
        <svg viewBox="0 0 24 24" aria-hidden="true"><path d="M6.6 10.8a15.1 15.1 0 0 0 6.6 6.6l2.2-2.2c.3-.3.7-.4 1-.2 1.1.4 2.3.6 3.6.6.6 0 1 .4 1 1V20c0 .6-.4 1-1 1A17 17 0 0 1 3 4c0-.6.4-1 1-1h3.5c.6 0 1 .4 1 1 0 1.3.2 2.5.6 3.6.1.3 0 .7-.2 1z"/></svg>
      </p>
      <p class="contact__line">ned@vontaramedia.example
        <svg viewBox="0 0 24 24" aria-hidden="true"><path d="M2 5h20v14H2z" /><path d="M2 5l10 8 10-8" fill="none" stroke="#2d2d2f" stroke-width="2"/></svg>
      </p>
      <p class="contact__line">vontaramedia.example
        <svg viewBox="0 0 24 24" aria-hidden="true"><circle cx="12" cy="12" r="10"/><path d="M6 8c2 0 3 1 3 3s2 2 2 4-1 3 0 5M14 4c0 2 2 2 3 3s3 1 4 2" fill="none" stroke="#2d2d2f" stroke-width="1.8"/></svg>
      </p>
    </div>

    <p class="wordmark">Vontara Media</p>

    <ul class="services">
      <li>Content &amp; Experience Strategy</li>
      <li>Brand Development &amp; SEO</li>
      <li>Website Design &amp; Operation</li>
      <li>Social Media Integration</li>
      <li>Complete Video Solutions</li>
    </ul>
  </section>

  <section class="card card--back">
    <div class="back-brand">
      <div class="back-brand__square"></div>
      <p class="wordmark">Vontara Media</p>
    </div>
  </section>
</body>
</html>
```